Business card and insta posting square

This is for 2 separate projects...

1...a double sided business card for online business (no address) to hand to businesses to get them to list their details on my online directory. the butterfly logo is to be used on the business card.

2.... a posting square for Instagram to write inspirational quotes over the top of to post....with a small butterfly logo somewhere on it (in a corner maybe)....the square is to have a thin, solid green outline around the edge of it, and a faded picture through the background that will allow me to write text over the top of it that will be easily readable.
I would like the same box for all Instagram quote posts for consistency ..

Target Market(s)

spiritual , yoga, meditation, wellness......

Industry/Entity Type

Wellness

Contact Information for Business Card

Details for Business Card...
Tending A Bright Garden
Your Complete Wellness Directory
www.tendingabrightgarden.example
PHOTOS/FRIENDS/BOARDS/POSTS
*List Your Business for FREE *

Colors
33b8a4
34a7d8
3276b5
876aae
9bcb3c

Requirements
Must have
• butterfly logo included on business card
• insta post square can use the butterfly logo OR the TABG green square uploaded in the images
Nice to have
• greens

```html
<!DOCTYPE html>
<html lang="en">
<head>
<meta charset="utf-8">
<title>Tending A Bright Garden – Card and Quote Square</title>
<link rel="stylesheet" href="https://fonts.googleapis.com/css2?family=PT+Sans:ital,wght@0,400;0,700;1,400&family=Roboto:wght@300;400;700;900&display=swap">
<style>
  :root {
    --bg-top: #ece7e2;
    --bg-bottom: #e8e2dd;
    --card-white: #ffffff;
    --brand-green: #6ab04c;
    --leaf-green: #5aab3e;
    --deep-green: #3f9a2c;
    --brand-purple: #5a32a8;
    --brand-blue: #3276b5;
    --brand-teal: #33b8a4;
    --frame-dark: #2e2e2e;
    --ink: #222222;
    --faint: #f1f1f1;
  }
  * { box-sizing: border-box; margin: 0; padding: 0; }
  html, body { width: 848px; height: 1200px; overflow: hidden; }
  body {
    position: relative;
    background: linear-gradient(to bottom, var(--bg-top) 0 566px, var(--bg-bottom) 566px 100%);
    font-family: "PT Sans", sans-serif;
  }

  /* Business card, front */
  .card {
    position: absolute;
    width: 310px;
    height: 178px;
    top: 200px;
    box-shadow: 0 6px 14px rgba(0,0,0,0.12);
    overflow: hidden;
  }
  .card--front { left: 92px; background: var(--card-white); }
  .card__mark {
    position: absolute;
    left: 117px; top: 18px;
    width: 76px; height: 70px;
    border-radius: 8px;
    background: linear-gradient(135deg, var(--brand-teal), var(--brand-blue) 45%, #7a2fbf);
    opacity: 0.9;
  }
  .card__name {
    position: absolute;
    left: 0; right: 0; top: 96px;
    text-align: center;
    font-size: 21px;
    font-weight: 400;
    color: var(--leaf-green);
  }
  .card__band {
    position: absolute;
    left: 0; right: 0; bottom: 0;
    height: 30px;
    background: var(--brand-purple);
    border-top: 3px solid var(--leaf-green);
    color: #fff;
    font-weight: 700;
    font-size: 12.5px;
    text-align: center;
    line-height: 27px;
  }

  /* Business card, back */
  .card--back {
    left: 446px;
    background: linear-gradient(160deg, #8ed45c, var(--leaf-green) 55%, var(--deep-green));
    color: #fff;
  }
  .card__tagline {
    position: absolute;
    left: 38px; right: 38px; top: 38px;
    border: 1.5px solid rgba(255,255,255,0.9);
    padding: 9px 0;
    text-align: center;
    font-weight: 700;
    font-size: 14px;
  }
  .card__contact {
    position: absolute;
    left: 58px; top: 108px;
    padding-left: 12px;
    border-left: 1.5px solid #24304a;
    font-weight: 700;
    font-size: 11.5px;
    line-height: 19px;
  }

  /* Quote square */
  .quote-square {
    position: absolute;
    left: 147px; top: 648px;
    width: 554px; height: 476px;
    background: var(--frame-dark);
    border-radius: 16px;
    padding: 5px;
  }
  .quote-square__inner {
    width: 100%; height: 100%;
    border: 7px solid var(--brand-green);
    border-radius: 12px;
    background: #fff;
    position: relative;
    overflow: hidden;
    text-align: center;
    font-family: "Roboto", sans-serif;
  }
  .quote-square__backdrop {
    position: absolute;
    left: 86px; top: 118px;
    width: 356px; height: 244px;
    border-radius: 40%;
    background: radial-gradient(ellipse at center, var(--faint) 0%, #f6f6f6 55%, rgba(255,255,255,0) 75%);
  }
  .quote-square__headline {
    position: absolute;
    left: 0; right: 0; top: 77px;
    font-size: 45px;
    font-weight: 900;
    color: var(--brand-green);
    letter-spacing: 0.5px;
  }
  .quote-square__body {
    position: absolute;
    left: 0; right: 0; top: 160px;
    font-size: 37px;
    font-weight: 300;
    line-height: 45px;
    color: var(--ink);
  }
  .quote-square__body strong { font-weight: 700; }
  .quote-square__sign {
    position: absolute;
    left: 0; right: 0; top: 364px;
    display: flex;
    justify-content: center;
    align-items: center;
    gap: 7px;
    font-size: 18px;
    font-weight: 700;
    color: var(--leaf-green);
    letter-spacing: 1px;
  }
  .quote-square__dot {
    width: 14px; height: 14px;
    border-radius: 50%;
    background: var(--leaf-green);
  }
</style>
</head>
<body>
  <section class="card card--front" aria-label="Business card front">
    <div class="card__mark" role="img" aria-label="Butterfly brand mark area"></div>
    <div class="card__name">Tending A Bright Garden</div>
    <div class="card__band">www.tendingabrightgarden.example</div>
  </section>

  <section class="card card--back" aria-label="Business card back">
    <div class="card__tagline">Your Complete Wellness Directory</div>
    <div class="card__contact">
      www.tendingabrightgarden.example<br>
      PHOTOS/FRIENDS/BOARDS/POSTS
    </div>
  </section>

  <section class="quote-square" aria-label="Quote post square">
    <div class="quote-square__inner">
      <div class="quote-square__backdrop" role="img" aria-label="Faded butterfly image behind the quote"></div>
      <h1 class="quote-square__headline">YOU ARE ENOUGH</h1>
      <p class="quote-square__body">
        YOU ARE SO ENOUGH<br>
        IT IS <strong>UNBELIEVABLE</strong><br>
        HOW ENOUGH YOU ARE.
      </p>
      <div class="quote-square__sign"><span class="quote-square__dot"></span>TABG</div>
    </div>
  </section>
</body>
</html>
```